cryotherapy business . Whole Body Cryotherapy, Localised Cryotherapy, Cryofacials

Need home page plus services, about, pricing, online booking, contact and blog page

I want something slick, hip and professional. Our studio colours are duck egg blue, white and grey

I would also like a social media scroll at the bottom of every page

I will upload some web designs that I like the look of

Target Market(s)

Men and Women 25-45

Industry/Entity Type

Health And Wellness

Coding

Coded - Design and coding required

Number of Pages Required

5+ page

Font styles to use
Serif
Sans Serif

Requirements
Must have
• Must be eye catching and easy to navigate
Nice to have
• animation
Should not have
• Not sure what the site should not have. I am fairly open to ideas as this is a brand new business.

```html
<!DOCTYPE html>
<html lang="en">
<head>
<meta charset="utf-8">
<title>Frostline Cryotherapy</title>
<link href="https://fonts.googleapis.com/css2?family=Roboto:wght@300;400;500&family=Roboto+Slab:wght@300;400&display=swap" rel="stylesheet">
<style>
:root{
  --duck:#7fb6c8;
  --duck-dark:#5f9fb4;
  --duck-soft:#d7e8ee;
  --ink:#4a4f52;
  --muted:#8d9396;
  --band:#414648;
  --footer:#3b4042;
  --line:#52585b;
  --white:#ffffff;
  --paper:#f4f6f7;
}
*{box-sizing:border-box;margin:0;padding:0}
html,body{width:668px;height:1200px;overflow:hidden}
body{font-family:"Roboto",Arial,sans-serif;color:var(--ink);background:var(--white)}
.site-header{height:62px;display:flex;align-items:center;justify-content:space-between;padding:0 22px 0 26px;background:var(--white)}
.brand{display:flex;align-items:center;gap:8px}
.brand-dot{width:22px;height:22px;border-radius:50%;background:var(--duck)}
.brand-name{font-size:22px;font-weight:300;letter-spacing:2px;color:var(--duck-dark);line-height:1}
.brand-tag{font-size:6px;letter-spacing:1px;color:var(--muted);margin-top:3px}
.main-nav{display:flex;gap:14px;font-size:9px;color:var(--ink)}
.main-nav .active{color:var(--duck-dark)}
.hero{position:relative;height:250px;display:flex;flex-direction:column;align-items:center;justify-content:center;text-align:center;color:var(--white)}
.hero-media{position:absolute;inset:0;background:radial-gradient(ellipse at 45% 30%,#c9dde5 0%,#98b9c6 45%,#6d92a2 100%)}
.hero-content{position:relative;margin-top:40px}
.hero h1{font-family:"Roboto Slab",Georgia,serif;font-weight:300;font-size:25px;letter-spacing:.5px}
.hero p{font-size:8px;margin-top:6px;opacity:.9}
.btn-outline{display:inline-block;margin-top:10px;padding:5px 16px;border:1px solid var(--white);font-size:8px;letter-spacing:1px}
.about-band{height:166px;background:var(--band);color:#d5d9db;text-align:center;padding:18px 60px 0}
.about-band h2{font-family:"Roboto Slab",Georgia,serif;font-weight:300;font-size:20px;color:var(--white);margin-bottom:12px}
.about-band p{font-size:7.3px;line-height:1.65;margin-bottom:8px}
.services{height:277px;background:var(--paper);display:flex;justify-content:center;gap:38px;padding-top:42px}
.service-card{width:158px;background:var(--white);text-align:center;padding-bottom:10px}
.service-media{height:126px}
.media-cold{background:linear-gradient(160deg,#2d6fb6,#5fa2dc)}
.media-face{background:linear-gradient(160deg,#cfe3ec,#9fc2d2)}
.media-device{background:linear-gradient(160deg,#e2e5e6,#b7bcbe)}
.service-card h3{font-weight:300;font-size:10px;line-height:1.35;color:var(--duck);margin:10px 12px 6px}
.service-card p{font-size:6.5px;line-height:1.6;color:var(--muted);text-align:left;padding:0 12px}
.card-foot{display:flex;justify-content:flex-end;padding:6px 12px 0}
.btn-small{background:var(--band);color:var(--white);font-size:6.5px;padding:3px 8px}
.testimonials{height:180px;text-align:center;padding-top:26px}
.testimonials h2{font-family:"Roboto Slab",Georgia,serif;font-weight:300;font-size:19px;color:var(--ink)}
.testimonials .lead{font-size:7.5px;color:var(--muted);margin-top:4px}
.quote{display:flex;align-items:center;justify-content:center;gap:24px;margin-top:18px}
.quote-arrow{font-size:12px;color:var(--muted)}
.quote blockquote{font-size:10px;font-style:italic;font-weight:300;color:var(--muted);line-height:1.6;width:330px}
.quote-author{margin-top:10px;font-size:9px;color:var(--duck-dark)}
.quote-role{font-size:6.5px;color:var(--muted);margin-top:2px}
.site-footer{height:243px;background:var(--footer);display:grid;grid-template-columns:210px 190px 1fr;padding:24px 26px 0 40px;color:#c3c8ca}
.foot-brand{display:flex;flex-direction:column;align-items:flex-start}
.foot-brand .brand-dot{width:30px;height:30px;margin-left:20px}
.foot-brand .brand-name{color:var(--white);font-size:20px;margin-top:6px}
.foot-title{font-size:7px;letter-spacing:1px;color:var(--white);margin-bottom:10px}
.foot-brand .foot-title{margin-top:28px}
.contact-list{list-style:none;font-size:7px;line-height:1.9}
.contact-list li{display:flex;align-items:center;gap:6px}
.contact-list svg{width:7px;height:7px;fill:var(--duck)}
.link-list{list-style:none;font-size:7px}
.link-list li{padding:6px 0;border-bottom:1px solid var(--line);width:120px}
.social-list{list-style:none;font-size:7.5px}
.social-list li{display:flex;align-items:center;gap:9px;margin-bottom:12px}
.social-icon{width:18px;height:18px;border-radius:50%;background:#5d6467}
.foot-col{border-left:1px solid var(--line);padding-left:16px}
.copyright{height:22px;background:var(--duck);color:var(--white);font-size:6.5px;display:flex;align-items:center;justify-content:center}
</style>
</head>
<body>
<header class="site-header">
  <div class="brand">
    <span class="brand-dot"></span>
    <div>
      <div class="brand-name">FROSTLINE</div>
      <div class="brand-tag">WHOLE BODY · LOCALISED · CRYOFACIALS</div>
    </div>
  </div>
  <nav class="main-nav">
    <span>Home</span><span>Our Services</span><span class="active">About Us</span><span>Price List</span><span>Blog</span><span>Contact Us</span>
  </nav>
</header>

<section class="hero">
  <div class="hero-media" role="img" aria-label="Cool blue photograph of cryotherapy mist"></div>
  <div class="hero-content">
    <h1>Frostline Cryotherapy</h1>
    <p>Cold therapy sessions that restore energy, ease soreness and help you recover faster.</p>
    <span class="btn-outline">BOOK NOW</span>
  </div>
</section>

<section class="about-band">
  <h2>What is Whole Body Cryotherapy?</h2>
  <p>Whole body cryotherapy exposes the body to extremely cold, dry air for two to three minutes. The brief chill triggers a natural response that draws blood to the core, helping the body reduce inflammation, calm aching muscles and lift mood. Many clients use it after training, others simply to feel refreshed and alert for the rest of the day.</p>
  <p>Sessions take place in a modern chamber supervised by trained staff at every step. No appointment is the same, so we tailor each visit to your goals and comfort.</p>
</section>

<section class="services">
  <article class="service-card">
    <div class="service-media media-cold" role="img" aria-label="Blue graphic with the word cold"></div>
    <h3>Frostline<br>Cryotherapy</h3>
    <p>A short cold session that eases tension, speeds recovery and leaves you feeling light and alert.</p>
    <div class="card-foot"><span class="btn-small">Read More</span></div>
  </article>
  <article class="service-card">
    <div class="service-media media-face" role="img" aria-label="Photo of a cryofacial treatment"></div>
    <h3>Frostline<br>Cryotherapy</h3>
    <p>A short cold session that eases tension, speeds recovery and leaves you feeling light and alert.</p>
    <div class="card-foot"><span class="btn-small">Read More</span></div>
  </article>
  <article class="service-card">
    <div class="service-media media-device" role="img" aria-label="Photo of a localised cryotherapy device"></div>
    <h3>Frostline<br>Cryotherapy</h3>
    <p>A short cold session that eases tension, speeds recovery and leaves you feeling light and alert.</p>
    <div class="card-foot"><span class="btn-small">Read More</span></div>
  </article>
</section>

<section class="testimonials">
  <h2>Our Customer Testimonials</h2>
  <p class="lead">Real words from the people who train, recover and relax with us.</p>
  <div class="quote">
    <span class="quote-arrow">‹</span>
    <blockquote>“The sessions gave me more energy than I expected. I sleep better and my knees feel easier after every long run.”</blockquote>
    <span class="quote-arrow">›</span>
  </div>
  <div class="quote-author">Mark Ellery</div>
  <div class="quote-role">Marathon runner</div>
</section>

<footer class="site-footer">
  <div class="foot-brand">
    <span class="brand-dot"></span>
    <span class="brand-name">FROSTLINE</span>
    <div class="foot-title">GET IN TOUCH</div>
    <ul class="contact-list">
      <li><svg viewBox="0 0 10 10"><path d="M5 0a3.5 3.5 0 0 0-3.5 3.5C1.5 6 5 10 5 10s3.5-4 3.5-6.5A3.5 3.5 0 0 0 5 0z"/></svg>12 Harbour Lane</li>
      <li><svg viewBox="0 0 10 10"><path d="M5 0a3.5 3.5 0 0 0-3.5 3.5C1.5 6 5 10 5 10s3.5-4 3.5-6.5A3.5 3.5 0 0 0 5 0z"/></svg>Northfield NR4 7QT</li>
      <li><svg viewBox="0 0 10 10"><path d="M2 0l2 2.5-1.2 1.3a6 6 0 0 0 3.4 3.4L7.5 6 10 8l-1.5 2C4 10 0 6 0 1.5z"/></svg>+44 1234 567890</li>
      <li><svg viewBox="0 0 10 10"><path d="M0 2h10v6H0z"/></svg>hello@frostline.example</li>
    </ul>
  </div>
  <div class="foot-col">
    <div class="foot-title">USEFUL LINKS</div>
    <ul class="link-list">
      <li>Home</li><li>Services</li><li>Pricing</li><li>Bookings</li><li>Blog</li><li>Contact</li>
    </ul>
  </div>
  <div class="foot-col">
    <div class="foot-title">SOCIAL LINKS</div>
    <ul class="social-list">
      <li><span class="social-icon"></span>Friendsy</li>
      <li><span class="social-icon"></span>Chirper</li>
      <li><span class="social-icon"></span>Circles</li>
      <li><span class="social-icon"></span>Workline</li>
    </ul>
  </div>
</footer>
<div class="copyright">Copyright © 2024 Frostline Cryotherapy | Terms of Use | Privacy Policy</div>
</body>
</html>
```